Clean book cover design for book about writing a book

Book title: The Crossing
Subtitle: 9 Paths to Crafting a Volume that Counts
Name: Marisol T. Brenwick, The Quill Nursery

This is a book which teaches 10 steps to writing a self-help book. I'm looking for a very clean impactful cover either with no image or just a small simple image of a book, typewriter, laptop, cabin or something very simple. I am attaching the manuscript here if reading it would help you with the cover. The theme of the book is that you can write with joy and ease and your book can just flow out of you if you learn how to clear the blocks between you and your book already written. Sort of a new agey stance on book writing.

The book should generally match the branding on my website. Www.TheQuillNursery.example.

I have photos of myself attached which I'd like used for the back cover with an "about the author section of maybe 50 words.

The project is for the full back cover and spine as well as the front cover (see print Forge template attached) but to win the contest you can just design the front cover and then I'll give the winner the template for the full design with the back cover copy. Or you can design the full cover using the template and you can use Loren ipsum text if you need to.

My clients are very upmarket and the themes of my business revolve around nuturing and incubating ideas and authors. Very feminine creation energy.

For colors see The Crossing Press (CB) wax seals and the background fades. I don't want my logo on the cover but I am attaching it here so you get a feel for the branding. The logo is in the LOBSTER font and you can see how we do the grey with the rainbow shadow.

Here are some covers I like:

http://www.shopvale.example/Pen-Tome-Quick-Stage---Stage/dp/055817342Q
http://www.shopvale.example/Plotting-Your-Tale-Chart-Triumph/dp/0841739265
http://www.shopvale.example/Be-Scribe-Seeking-Voice-Guide-ebook/dp/K22R9WQ3L1
http://www.shopvale.example/Strays-Tale-Triumph-Rupert-Vanhollow/dp/0552048871
Updates

I have revised my brief to include some picture and images that will help you create the cover. I have also included some of my favorite covers to give you more of a sense of what I'm going for. And I have included the manuscript in case it would help you to skim through it in order to get a sense of the reader and the book. I think if you look at my revised brief it will make it easier to create a submission. Thanks!

Target Market(s)

Women 40-60 who run small businesses as life coaches or other healing jobs (therapy, reiki, light work) they have a spiritual/new age bent.

Industry/Entity Type

Business

Font styles to use
Serif
Other font styles liked:
• Lobster (not required... just a suggestion since it's my logo font)

Requirements
Must have
• Name and title easy to read in 1" x 1" thumb nail
Nice to have
• Fantastic type face treatment.

Match the look and feel of my website.
Should not have
• Busy images. With one simple image or just designed with colors and typeface treatment

```html
<!DOCTYPE html>
<html lang="en">
<head>
<meta charset="utf-8">
<title>The Crossing — Book Cover</title>
<link rel="stylesheet" href="https://fonts.googleapis.com/css2?family=Lobster&family=Arimo:wght@400;700&display=swap">
<style>
  :root {
    --stage-bg: #e8e9ea;
    --cover-bg: #474747;
    --title-grey: #8a8a8a;
    --author-white: #ffffff;
    --frame-grey: #8d9197;
    --portrait-light: #f2efec;
    --portrait-warm: #e3c9a4;
  }
  * { margin: 0; padding: 0; box-sizing: border-box; }
  html, body {
    width: 1200px;
    height: 900px;
    overflow: hidden;
    background: var(--stage-bg);
  }
  .stage {
    position: relative;
    width: 1200px;
    height: 900px;
  }
  .book-cover {
    position: absolute;
    left: 352px;
    top: 78px;
    width: 518px;
    height: 734px;
    background: var(--cover-bg);
  }
  .title-block {
    position: absolute;
    right: 60px;
    top: 218px;
    text-align: right;
    color: var(--title-grey);
    font-family: "Lobster", cursive;
  }
  .book-title {
    font-size: 50px;
    font-weight: 400;
    line-height: 1.1;
    letter-spacing: 0.3px;
  }
  .book-subtitle {
    margin-top: 8px;
    font-size: 19.5px;
    font-weight: 400;
    line-height: 1.2;
  }
  .author-block {
    position: absolute;
    right: 200px;
    top: 578px;
    text-align: right;
    color: var(--author-white);
    font-family: "Arimo", Arial, sans-serif;
  }
  .author-name {
    font-size: 17px;
    font-weight: 700;
    line-height: 1.45;
  }
  .author-company {
    font-size: 15.5px;
    font-weight: 400;
    line-height: 1.45;
  }
  .author-portrait {
    position: absolute;
    left: 336px;
    top: 535px;
    width: 128px;
    height: 128px;
    border: 6px solid var(--frame-grey);
    background: radial-gradient(circle at 50% 45%, var(--portrait-warm) 0%, var(--portrait-light) 70%);
  }
</style>
</head>
<body>
  <main class="stage">
    <section class="book-cover">
      <header class="title-block">
        <h1 class="book-title">The Crossing</h1>
        <p class="book-subtitle">9 Paths to Crafting a Volume that Counts</p>
      </header>
      <div class="author-block">
        <p class="author-name">Marisol T. Brenwick</p>
        <p class="author-company">The Quill Nursery</p>
      </div>
      <div class="author-portrait" role="img" aria-label="Portrait photo of the author against a white background"></div>
    </section>
  </main>
</body>
</html>
```